Package Design for 15 lines of Tea

I need design variations for 15 different Tea lines.
The tea will be packaged in Tin cylinders.
I have attached several pictures to show you an example of the display we are modelling after along with other references.
The 15 tea lines are:
Study Tea
Ingredients: Brazilian Mate, Mint
Energy Boost Tea
Ingredients: Yunnan Coffee, Dark Puer
Relaxation Tea
Ingredients: Lotus Flower, South African Rooibos
Beauty Tea
Ingredients: Rose, Chrysanthemum, Red Dates, Huangqi
Sore Throat Tea
Ingredients: Honeysuckle, Pang Da Hai, Chamomile, Licorice Root
Get Well Tea
Ingredients: Ginger, Rooibos, Orange peel, Chinese Angelica
Diet Tea
Ingredients: Puer, Hibiscus, Lemongrass, Lotus Plumule
Bedtime Tea
Ingredients: Apple, Orange, Chamomile
South African Rooibos Tea
(pure)
Brazilian Yerba Mate Tea
(pure)
Long Jing Green Tea
(pure)
Darjeeling Black Tea
(pure)
Nepal Golden Tea
(Pure)
Bai Mu Dan White Tea
(pure)
Phoenix Oolong Tea
(pure)
Every Tea Blend should have three unique symbols that describe the purpose and theme of the blend. (!!Please don't make specific reference to the ingredients of the blends because some of these ingredients may be changed later. Stick to focusing on the intended purpose of the tea blend!!)
I would like the symbols to keep the same brushlike style that is consistent with our company logo.
Please keep the three block structure. I suggest keeping to just one color per tea blend. This will help each blend stand out between one another. I have a sample of the "Diet Tea" attached that I did myself to give you an idea of the structure I'm looking for, but obviously it's just my amateur version. Hope you can make them look far more appealing.
The ultimate goal is to build a picture language unique to our brand. As more products are released, we intend to potentially have hundreds of symbols, each with it's own meaning. So it would be nice when you present your pictures if you explain its intended meaning or message.
Deminsions:
Cylinder type 1: 82mm*38mmH
circular labels (along with your design) will be placed on the cap of product, and then the cylinder will be slanted on it's side to display the cap towards the customer.
Cylinder type 2: 65mm*152mmH
the labels will be placed on the side of the cylinder. In this version, try lining the three symbols in a vertical position. If this looks awful to you then feel free to go back to the horizontal style, but it would be nice to see what the vertical version looks like for reference.
Updates
Due to the scope of this project, please take note that I just increased my budget an additional 500 dollars more.
I also just added a 100 dollar second place prize. Don't want to see hard work unrewarded.
Feel free to send a few samples and I will provide prompt feedback. Please don't feel that you must submit all 15 lines at the same time.
Project Deadline Extended
Reason: I am extending the deadline as I feel there are more detailed revisions that need to be made until final selection.
Target Market(s)
Middle to Upper Class Consumers in China
Industry/Entity Type
It Company
Other font styles liked:
- font similar to font on company logo
Requirements
Must have
- Tea Designs must be in harmony with company logo and theme.
Should not have
- Avoid using Chinese characters as symbols. They may seem cool to westerners, but it's tacky for Chinese consumers.

```html
<!DOCTYPE html>
<html lang="en">
<head>
<meta charset="utf-8">
<title>Study Tea – Cap Label</title>
<link href="https://fonts.googleapis.com/css2?family=Special+Elite&family=Quicksand:wght@300&display=swap" rel="stylesheet">
<style>
  :root {
    --mint: #c5e0c8;
    --charcoal: #2b2a29;
    --ink-grey: #6b6b6b;
    --white: #ffffff;
    --icon-light: #b4ccb7;
    --icon-dark: #8e9a90;
  }
  html, body {
    margin: 0;
    padding: 0;
    width: 1200px;
    height: 1200px;
    overflow: hidden;
    background: var(--white);
  }
  .cap-label {
    display: block;
    width: 1200px;
    height: 1200px;
  }
  .rim { fill: var(--mint); }
  .face { fill: var(--charcoal); }
  .symbol-block { fill: var(--mint); }
  .typewriter {
    font-family: "Special Elite", "Courier New", monospace;
  }
  .symbol-label {
    fill: var(--ink-grey);
    font-size: 82px;
    text-anchor: middle;
  }
  .blend-name {
    fill: var(--mint);
    font-size: 120px;
  }
  .blend-kind {
    fill: var(--white);
    font-family: "Quicksand", "Helvetica Neue", sans-serif;
    font-weight: 300;
    font-size: 205px;
  }
  .ingredients {
    fill: var(--mint);
    font-size: 56px;
  }
  .brand-plate { fill: var(--white); }
  .brand-name {
    fill: var(--charcoal);
    font-size: 40px;
    text-anchor: middle;
  }
  .brand-dot { fill: var(--mint); }
</style>
</head>
<body>
<svg class="cap-label" viewBox="0 0 1200 1200" xmlns="http://www.w3.org/2000/svg">
  <defs>
    <clipPath id="face-clip">
      <circle cx="600" cy="600" r="557"/>
    </clipPath>
    <linearGradient id="study-symbol-tone" x1="0" y1="0" x2="1" y2="1">
      <stop offset="0" stop-color="var(--icon-light)"/>
      <stop offset="1" stop-color="var(--icon-dark)"/>
    </linearGradient>
    <path id="ingredient-arc" d="M 600 240 A 360 360 0 0 1 600 960"/>
  </defs>

  <circle class="rim" cx="600" cy="600" r="600"/>
  <circle class="face" cx="600" cy="600" r="557"/>

  <g class="symbol-column" clip-path="url(#face-clip)">
    <rect class="symbol-block" x="502" y="0" width="200" height="312"/>
    <rect class="symbol-block" x="502" y="332" width="200" height="277"/>
    <rect class="symbol-block" x="502" y="634" width="200" height="274"/>
  </g>

  <text class="typewriter symbol-label" x="602" y="206">123</text>

  <rect class="study-symbol" x="512" y="385" width="180" height="175" rx="14"
        fill="url(#study-symbol-tone)" opacity="0.55"
        role="img" aria-label="Brush-style closed book symbol for studying"/>

  <text class="typewriter symbol-label" x="602" y="806">abc</text>

  <text class="typewriter blend-name" x="136" y="524">Study</text>
  <text class="blend-kind" x="146" y="702">tea</text>

  <text class="typewriter ingredients">
    <textPath href="#ingredient-arc" startOffset="50%" text-anchor="middle">Brazilian Mate, Mint</textPath>
  </text>

  <g class="brand-mark">
    <path class="brand-plate" d="M 492 941 H 712 V 1112 Q 602 1124 492 1112 Z"/>
    <text class="typewriter brand-name" x="602" y="1000">Lumo Tea</text>
    <rect class="brand-dot" x="580" y="1030" width="44" height="44"/>
  </g>
</svg>
</body>
</html>
```